Falzflyer-Design für Softwareprodukte
Zielgruppe
Wir bieten mit unserer Produktlinie Veranta Softwareprodukte für Fluggesellschaften und touristische Unternehmen. Unsere Softwarelösungen sind ein Vertriebssystem für Airlines (Inventory), Prozess-basierte Automatisierungen, Buchungsschnittstellen und Datenanalysen. Weiterhin bieten wir diesen Unternehmen Custom Development und Beratungsdienstleistungen an.
Aufgabenstellung
Wir benötigen einen Falzflyer. Die Maße sind in einem Datenblatt von unserer Druckerei enthalten.
Weiterhin haben wir unser Logo und unserem Color Code hochgeladen. In einem pdf haben wir zusätzlich die Inhalte zusammengefasst (aussen und innen), die im Flyer aufgeführt werden sollen (noch nicht alles ist auf unserer Website verfügbar).
Einige Bilder, die wir auf der Website nutzen bzw. nutzen werden, findet ihr dort auch . Es kann aber gerne anderes Bildmaterial verwendet werden.
Wir überarbeiten gerade unsere Website und nutzen neben den unterschiedlichen Grautönen vorrangig #4b75e5, #00bac9 und folgende Schriftarten: Pragrati Narrow für Überschriften, Open Sans für Texte
Flyer wird ausschließlich in Englisch benötigt.

```html
<!DOCTYPE html>
<html lang="en">
<head>
<meta charset="utf-8">
<title>Skyvanta Veranta – Folded Flyer Inside Spread</title>
<link rel="stylesheet" href="https://fonts.googleapis.com/css2?family=Open+Sans:ital,wght@0,400;0,600;1,400&family=Pragati+Narrow:wght@400;700&display=swap">
<style>
  :root {
    --page-bg: #eceef1;
    --navy-deep: #0c1636;
    --navy: #14244f;
    --blue-mid: #1f4f8a;
    --brand-blue: #4b75e5;
    --brand-cyan: #00bac9;
    --heading: #3cc4ec;
    --text: #ffffff;
    --fold: rgba(0, 0, 0, 0.28);
    --plane-light: #5fd0f0;
    --plane-mid: #2a8fc8;
    --plane-dark: #17407a;
  }
  * { box-sizing: border-box; margin: 0; padding: 0; }
  html, body {
    width: 1200px; height: 796px; overflow: hidden;
    background: var(--page-bg);
  }
  .flyer {
    position: absolute; left: 62px; top: 18px;
    width: 1076px; height: 760px;
    display: grid; grid-template-columns: repeat(3, 1fr);
    background: linear-gradient(180deg, var(--blue-mid) 0%, var(--navy) 38%, var(--navy-deep) 100%);
    box-shadow: 0 10px 30px rgba(20, 30, 60, 0.25);
    overflow: hidden;
  }
  .panel {
    position: relative;
    padding: 56px 30px 30px;
    border-right: 1px solid var(--fold);
    z-index: 2;
  }
  .panel:last-child { border-right: none; }
  .panel-title {
    font-family: "Pragati Narrow", sans-serif;
    font-weight: 400;
    font-size: 27px;
    line-height: 1.1;
    color: var(--heading);
    margin-bottom: 22px;
  }
  .panel-copy {
    font-family: "Open Sans", sans-serif;
    font-size: 12.5px;
    line-height: 1.75;
    color: var(--text);
    text-align: justify;
    margin-bottom: 12px;
  }
  .features-title {
    font-family: "Pragati Narrow", sans-serif;
    font-size: 24px;
    color: var(--heading);
    margin: 22px 0 8px;
  }
  .feature-list {
    list-style: none;
    font-family: "Open Sans", sans-serif;
    font-size: 12.5px;
    line-height: 1.6;
    color: var(--text);
  }
  .feature-list li {
    position: relative; padding-left: 12px; margin-bottom: 2px;
  }
  .feature-list li::before {
    content: ""; position: absolute; left: 0; top: 9px;
    width: 4px; height: 4px; border-radius: 50%; background: var(--text);
  }
  .hero-visual {
    position: absolute; left: 250px; top: 300px;
    width: 800px; height: 420px;
    z-index: 1;
    border-radius: 28px;
    background:
      radial-gradient(ellipse 60% 55% at 42% 58%, rgba(95, 208, 240, 0.85) 0%, rgba(42, 143, 200, 0.7) 45%, rgba(23, 64, 122, 0.55) 80%, rgba(23, 64, 122, 0.35) 100%),
      linear-gradient(160deg, var(--plane-mid) 0%, var(--plane-dark) 100%);
    opacity: 0.85;
  }
</style>
</head>
<body>
  <main class="flyer">
    <section class="panel panel-inventory">
      <h2 class="panel-title">Skyvanta Veranta Inventory</h2>
      <p class="panel-copy">Fully automated inventory and allotment management for touristic charter airlines with seamless host system integration.</p>
      <ul class="feature-list">
        <li>Seat capacity management</li>
        <li>Contract management</li>
        <li>Ancillary assignment</li>
      </ul>
    </section>

    <section class="panel panel-development">
      <h2 class="panel-title">Skyvanta Veranta Development</h2>
      <p class="panel-copy">We provide custom development based on modern technology and deep airline and touristic knowledge.</p>
      <p class="panel-copy">As experienced Airline-IT developers we implement your requirements fast and reliable.</p>
    </section>

    <section class="panel panel-automate">
      <h2 class="panel-title">Skyvanta Veranta Automate</h2>
      <p class="panel-copy">Skyvanta Veranta Automate enables the complete automation of existing and new back-office processes, resulting in increasing revenue as well as significant cost and time savings.</p>
      <h3 class="features-title">Key Features:</h3>
      <ul class="feature-list">
        <li>Rule engine - based Revenue Integrity</li>
        <li>Back-office automation with Queue Management, Ticketing, Reissue &amp; Revalidation</li>
        <li>Mass rebooking &amp; PNR updates &amp; FTC- handling</li>
        <li>Customized commission &amp; invoicing</li>
        <li>Loyalty Program &amp; Branded Fare Management in PSS</li>
        <li>Sales channel synchronization</li>
      </ul>
    </section>

    <div class="hero-visual" role="img" aria-label="Large glowing low-poly paper plane illustration made of light lines on a starry dark blue background, spanning the lower part of the spread"></div>
  </main>
</body>
</html>
```